Pallmore Design Project

It needs to be similar in look and feel to our website www.brightwaycarecentre.com. It should have a call to action to Like us and view our web page. It should mention our free visit guarantee if we cannot help.
Updates

I appreciate the swift response and the high quality of all submissions. We are not in a hutty and I want to adequately critique all designs. Give me a little time to point out changes.

Dear designers,

I thank you all for your submissions. One has proven to meet our requirements exactly with little if any modifications. A decision has been made. Thank you all for your submissions.

Target Market(s)

MEn concerned about the 4 medical problems listed on our website including the challenge of less than satisfying size

Industry/Entity Type

Call

```html
<!DOCTYPE html>
<html lang="en">
<head>
<meta charset="utf-8">
<title>Brightway Care Centre Banner</title>
<link href="https://fonts.googleapis.com/css2?family=Roboto+Condensed:wght@400;700&family=Arimo:wght@400;700&display=swap" rel="stylesheet">
<style>
  :root {
    --backdrop: #363435;
    --paper: #f3f3f3;
    --navy: #1b2f93;
    --green: #3d9a2b;
    --ink: #333333;
    --gold: #e0a412;
    --gold-dark: #b5781a;
    --tile: #efefef;
    --tile-edge: #8a8a8a;
  }
  html, body {
    margin: 0;
    padding: 0;
    width: 1200px;
    height: 1001px;
    overflow: hidden;
    background: var(--backdrop);
    font-family: "Arimo", Arial, sans-serif;
  }
  .canvas { position: relative; width: 1200px; height: 1001px; }
  .banner {
    position: absolute;
    left: 87px; top: 77px;
    width: 1031px; height: 383px;
    background: var(--paper);
  }
  .tagline-band {
    position: absolute;
    left: 0; top: 25px;
    width: 100%; height: 28px;
    background: var(--green);
    color: #fff;
    font-family: "Roboto Condensed", "Arial Narrow", sans-serif;
    font-size: 16.5px;
    line-height: 28px;
    text-align: center;
    letter-spacing: 0.1px;
  }
  .brand {
    position: absolute;
    left: 35px; top: 88px;
    display: flex; align-items: center; gap: 16px;
  }
  .brand-dot {
    width: 62px; height: 62px;
    border-radius: 50%;
    background: var(--navy);
  }
  .brand-name {
    color: var(--navy);
    font-weight: 700;
    font-size: 44px;
    letter-spacing: -0.5px;
    white-space: nowrap;
  }
  .service-list {
    position: absolute;
    left: 243px; top: 179px;
    margin: 0; padding: 0; list-style: none;
  }
  .service {
    width: 377px; height: 35px;
    margin-bottom: 13px;
    border-radius: 4px;
    color: #fff;
    font-size: 20px;
    line-height: 35px;
    text-align: right;
    padding-right: 32px;
    box-sizing: border-box;
    white-space: nowrap;
  }
  .service--navy { background: var(--navy); }
  .service--green { background: var(--green); }
  .contact {
    position: absolute;
    right: 28px; top: 62px;
    text-align: right;
  }
  .contact-heading {
    margin: 0;
    color: var(--navy);
    font-size: 36px;
    font-weight: 700;
    line-height: 40px;
  }
  .contact-phone {
    margin: 4px 0 0;
    color: var(--ink);
    font-size: 18px;
  }
  .contact-guarantee {
    margin: 5px 0 0;
    color: var(--ink);
    font-family: "Roboto Condensed", "Arial Narrow", sans-serif;
    font-size: 17px;
  }
  .contact-guarantee strong { color: var(--navy); }
  .consultation {
    position: absolute;
    left: 701px; top: 155px;
    display: flex; align-items: center;
  }
  .consultation-label {
    color: var(--navy);
    font-size: 37px;
  }
  .guarantee-seal { margin-left: 2px; }
  .social {
    position: absolute;
    right: 32px; top: 255px;
    text-align: right;
  }
  .like-button {
    display: inline-block;
    padding: 0 8px;
    height: 30px;
    line-height: 30px;
    border: 1px solid #c3c8d6;
    background: #e9ecf3;
    color: var(--navy);
    font-size: 18px;
  }
  .social-note {
    margin: 6px 0 0;
    color: var(--ink);
    font-size: 18px;
    line-height: 21px;
  }
  .social-note .accent { color: var(--navy); }
  .site-url {
    margin: 4px 0 0;
    color: var(--navy);
    font-size: 21px;
  }
  .app-tile {
    position: absolute;
    left: 115px; top: 309px;
    width: 192px; height: 185px;
    box-sizing: border-box;
    border: 1px solid var(--tile-edge);
    border-radius: 26px;
    background: var(--tile);
    display: flex; flex-direction: column;
    align-items: center; justify-content: center;
    gap: 10px;
  }
  .app-tile-dot {
    width: 56px; height: 56px;
    border-radius: 50%;
    background: var(--navy);
  }
  .app-tile-name {
    color: var(--navy);
    font-weight: 700;
    font-size: 20px;
  }
</style>
</head>
<body>
<div class="canvas">
  <section class="banner">
    <div class="tagline-band">Restore your confidence and enjoy sexual satisfaction again. Call us today for a private consultation. It's secure and confidential.</div>

    <div class="brand">
      <span class="brand-dot"></span>
      <span class="brand-name">Brightway Care Centre</span>
    </div>

    <ul class="service-list">
      <li class="service service--navy">Erectile Dysfunction</li>
      <li class="service service--green">Premature Ejaculation</li>
      <li class="service service--navy">Low Testosterone</li>
      <li class="service service--green">Non Surgical Penile Enhancement</li>
    </ul>

    <div class="contact">
      <h2 class="contact-heading">Call Us Today!</h2>
      <p class="contact-phone">855 BW-CARE-1 (855-292-2731)</p>
      <p class="contact-guarantee">Free Visit Guarantee If We Cannot <strong>Help!</strong></p>
    </div>

    <div class="consultation">
      <span class="consultation-label">Consultation</span>
      <svg class="guarantee-seal" width="86" height="84" viewBox="0 0 86 84" aria-hidden="true">
        <circle cx="43" cy="42" r="40" fill="var(--gold-dark)"/>
        <circle cx="43" cy="42" r="33" fill="var(--gold)"/>
      </svg>
    </div>

    <div class="social">
      <span class="like-button">Pallmore</span>
      <p class="social-note"><span class="accent">This page</span> And<br>Visit Us On:</p>
      <p class="site-url">www.brightwaycarecentre.com</p>
    </div>
  </section>

  <div class="app-tile">
    <span class="app-tile-dot"></span>
    <span class="app-tile-name">Brightway</span>
  </div>
</div>
</body>
</html>
```